Business card for a plastic surgeon

i need a business card for a plastic surgeon. I have two adresses. The card should communicate safety, simmetry, beauty and with soft colors.
What i want in the card:
- my logo: Letters "R"and "B" (picture uploaded)
- my name: Renato Bastiani
- my registration: CRM 507 219
- my adresses and phone numbers (2):
- Av Dr Teixeira Lopes, 2710, sala 305 - Vila Olímpia | São Paulo/ SP - Phone: 11 4172-5036
- Al. Itapeva, 47, 3 andar - Alphaville | Barueri/ SP - Phone: 11 6350-2481

- my social network: site, facebook and instagram

Target Market(s)

people (95% girls and women) that want cosmetic procedures and plastic surgery

Industry/Entity Type

Business

Contact Information for Business Card

The card should communicate safety, simmetry, beauty and with soft colors.
Beige, brown, gray, rosy are some options. Color is free

Font styles to use
Serif

Requirements
Must have
• - my logo: Letters "R"and "B" (picture uploaded)
• - my name: Renato Bastiani
• - my registration: CRM 507 219
• - my adresses and phone numbers (2):
• - Av Dr Teixeira Lopes, 2710, sala 305 - Vila Olímpia | São Paulo/ SP - Phone: 11 4172-5036
• - Al. Itapeva, 47, 3 andar - Alphaville | Barueri/ SP - Phone: 11 6350-2481
• - my social network: site, facebook and instagram
Should not have
• other images (only my logo)

```html
<!DOCTYPE html>
<html lang="pt-BR">
<head>
<meta charset="utf-8">
<title>Dr. Renato Bastiani — Cartão de visita</title>
<link rel="stylesheet" href="https://fonts.googleapis.com/css2?family=Open+Sans:wght@400;600&family=Cormorant+Garamond:wght@500&display=swap">
<style>
  :root {
    --backdrop: #e9dcdc;
    --card-front: #e6f4f6;
    --card-back: #ffffff;
    --ink: #111111;
    --ink-soft: #3a3a3a;
    --mark: #c6cfd2;
    --bar: #0d0d0d;
  }
  * { box-sizing: border-box; margin: 0; padding: 0; }
  html, body { width: 1200px; height: 938px; overflow: hidden; }
  body {
    background: var(--backdrop);
    position: relative;
    font-family: "Open Sans", Arial, sans-serif;
  }
  .card {
    position: absolute;
    width: 540px;
    height: 315px;
    box-shadow: 0 10px 24px rgba(80, 50, 50, 0.18);
  }
  .card--front { left: 150px; top: 110px; background: var(--card-front); }
  .card--back  { left: 520px; top: 500px; background: var(--card-back); }

  .card__bar {
    position: absolute;
    right: 0;
    top: 88px;
    width: 30px;
    height: 9px;
    background: var(--bar);
  }
  .card__mark {
    position: absolute;
    left: 372px;
    top: 50%;
    transform: translateY(-50%);
    width: 110px;
    text-align: center;
    font-family: "Open Sans", Arial, sans-serif;
    font-weight: 600;
    font-size: 18px;
    line-height: 1.25;
    color: var(--mark);
  }
  .identity {
    position: absolute;
    left: 105px;
    top: 138px;
  }
  .identity__name {
    font-weight: 600;
    font-size: 21px;
    color: var(--ink);
    letter-spacing: 0.2px;
  }
  .identity__role,
  .identity__crm {
    margin-top: 10px;
    margin-left: 8px;
    font-family: "Cormorant Garamond", Georgia, serif;
    font-weight: 500;
    font-size: 10px;
    letter-spacing: 3px;
    text-transform: uppercase;
    color: var(--ink-soft);
  }
  .identity__crm { margin-top: 6px; }
  .contacts {
    position: absolute;
    left: 40px;
    top: 72px;
    width: 300px;
    text-align: center;
    font-size: 13px;
    line-height: 1.5;
    color: var(--ink);
  }
  .contacts__office + .contacts__office { margin-top: 22px; }
  .contacts__social {
    margin-top: 22px;
    font-size: 11px;
    color: var(--ink-soft);
  }
</style>
</head>
<body>
  <section class="card card--front" aria-label="Frente do cartão">
    <div class="identity">
      <p class="identity__name">Dr. Renato Bastiani</p>
      <p class="identity__role">Cirurgião Plástico</p>
      <p class="identity__crm">CRM 507 219</p>
    </div>
    <p class="card__mark">Renato<br>Bastiani</p>
    <span class="card__bar"></span>
  </section>

  <section class="card card--back" aria-label="Verso do cartão">
    <div class="contacts">
      <p class="contacts__office">Al. Itapeva, 47, 3 andar - Alphaville. Barueri/ SP<br>Phone: 11 6350-2481</p>
      <p class="contacts__office">Av Dr Teixeira Lopes, 2710, sala 305 - Vila Olímpia, São Paulo/ SP<br>Phone: 11 4172-5036</p>
      <p class="contacts__social">Site · Facebook · Instagram: @drrenatobastiani</p>
    </div>
    <p class="card__mark">Renato<br>Bastiani</p>
    <span class="card__bar"></span>
  </section>
</body>
</html>
```